Values Statement poster template

We want to develop a poster template for our company policies and statements which promote our company values in our workplaces.
These documents are important in showing our clients, suppliers and employees who we are and what we stand for.
The graphic design will incorporate our company logo, and be bright, uplifting and inspiring, developing a graphic theme that we can utilise for other company documents. The design will graphically illustrate and support our values statement, with colour and modern design.
This values poster will be the first in a series of documents using the same theme.The format will be a4 and a3 portrait
We are an environmental service business specialising in rehabilitation and revegetation

Target Market(s)

Tier one clients in industry, Mining, Construction and agriculture

Font styles to use
Other font styles liked:
• calibri

Requirements
Must have
• Professional , high end feel, able to read clearly on a poster
Nice to have
• graphic design elements, symbols, etc which support the message, that can be carried through to various documents such as quality, environmental, safety policies
A bright theme which ties in with our logo colours.

```html
<!DOCTYPE html>
<html lang="en">
<head>
<meta charset="utf-8">
<title>Fernvale Land Care – Values Statement</title>
<link rel="stylesheet" href="https://fonts.googleapis.com/css2?family=Open+Sans:wght@400;600;700&display=swap">
<style>
  :root {
    --stage: #3a3a3c;
    --paper: #ffffff;
    --green-deep: #16703a;
    --green-edge: #2f4a1c;
    --green-light: #c4e3a0;
    --ink: #1f1f1f;
    --on-green: #ffffff;
  }
  * { box-sizing: border-box; margin: 0; padding: 0; }
  html, body { width: 1200px; height: 776px; overflow: hidden; }
  body {
    background: var(--stage);
    font-family: "Open Sans", Calibri, sans-serif;
    color: var(--ink);
    position: relative;
  }
  .sheet {
    position: absolute;
    top: 28px;
    width: 509px;
    height: 720px;
    background: var(--paper);
    overflow: hidden;
  }
  .sheet--front { left: 60px; }
  .sheet--back { left: 631px; }
  .sheet__art { position: absolute; inset: 0; width: 509px; height: 720px; }
  .brand {
    position: absolute; left: 24px; top: 40px;
    display: flex; align-items: center; gap: 9px;
    color: var(--green-deep); font-weight: 700; font-size: 24px;
  }
  .brand__dot { width: 18px; height: 18px; border-radius: 50%; background: var(--green-deep); }
  .section-tab {
    position: absolute; left: 0;
    height: 38px;
    background: var(--green-deep);
    color: var(--on-green);
    border-radius: 0 16px 16px 0;
    font-size: 22px; font-weight: 600;
    line-height: 38px;
    padding: 0 0 0 24px;
    letter-spacing: .3px;
    white-space: nowrap;
  }
  .copy {
    position: absolute; left: 24px; right: 24px;
    font-size: 11px; line-height: 1.45;
  }
  .copy__lead { font-weight: 600; margin-top: 8px; }
  .bullets { list-style: none; margin-top: 2px; }
  .bullets li { position: relative; padding-left: 12px; }
  .bullets li::before {
    content: ""; position: absolute; left: 0; top: 7px;
    width: 4px; height: 4px; border-radius: 50%; background: var(--ink);
  }
  .footer-contact {
    position: absolute; color: var(--on-green);
    font-size: 10.5px; line-height: 1.4;
    display: flex; gap: 8px; align-items: center;
  }
  .footer-contact svg { flex: none; }
</style>
</head>
<body>

<section class="sheet sheet--front">
  <svg class="sheet__art" viewBox="0 0 509 720">
    <defs>
      <linearGradient id="fieldFront" x1="0" y1="0" x2="0" y2="1">
        <stop offset="0" stop-color="#3f6d32"/>
        <stop offset="0.45" stop-color="#5c8a2c"/>
        <stop offset="0.65" stop-color="#c3d126"/>
        <stop offset="0.85" stop-color="#9b8e3c"/>
        <stop offset="1" stop-color="#b9cc2a"/>
      </linearGradient>
    </defs>
    <path d="M0,0 H509 C360,30 170,80 0,140 Z" fill="var(--green-light)"/>
    <path role="img" aria-label="Photo of green farm fields with barns below forested hills"
          d="M0,140 C170,80 360,30 509,0 C470,190 300,315 0,340 Z" fill="url(#fieldFront)"/>
    <path d="M509,0 C470,190 300,315 0,340" fill="none" stroke="var(--green-edge)" stroke-width="4"/>
    <path d="M0,720 C220,714 420,700 509,670 V720 Z" fill="var(--green-deep)"/>
  </svg>

  <div class="brand"><span class="brand__dot"></span>Fernvale Land Care</div>

  <h2 class="section-tab" style="top:362px;width:300px;">Our Values :</h2>
  <div class="copy" style="top:410px;">
    <p>These are the things we value most, they define the way we do business. We value our people above everything else.</p>
    <p class="copy__lead">We demonstrate this by:</p>
    <ul class="bullets">
      <li>Providing safe, positive, enjoyable workplaces where everyone feels valued and respected.</li>
      <li>Providing Careers, not Jobs, we grow together.</li>
      <li>Encouraging inclusion, participation and collaboration.</li>
      <li>Recognising and rewarding contribution and excellence.</li>
      <li>Supporting our people through tough times.</li>
    </ul>
  </div>

  <h2 class="section-tab" style="top:580px;width:420px;">We do good things for the planet :</h2>
  <div class="copy" style="top:626px;">
    <p>Our products are helping revegetate Australia, which we are tremendously proud of.<br>We minimise our environmental impact in everything we do.</p>
  </div>
</section>

<section class="sheet sheet--back">
  <svg class="sheet__art" viewBox="0 0 509 720">
    <defs>
      <linearGradient id="fieldBack" x1="0" y1="0" x2="0" y2="1">
        <stop offset="0" stop-color="#3f6d32"/>
        <stop offset="0.45" stop-color="#a9c42a"/>
        <stop offset="0.75" stop-color="#d7df2a"/>
        <stop offset="1" stop-color="#8e7f3c"/>
      </linearGradient>
    </defs>
    <path role="img" aria-label="Photo of green farm fields with barns below forested hills"
          d="M0,0 H509 V120 C400,150 250,165 170,125 C90,85 30,40 0,0 Z" fill="url(#fieldBack)"/>
    <path d="M509,120 C400,150 250,165 170,125 C90,85 30,40 0,0" fill="none" stroke="var(--green-edge)" stroke-width="4"/>
    <path d="M0,585 C200,605 400,580 509,540 V720 H0 Z" fill="var(--green-deep)"/>
  </svg>

  <h2 class="section-tab" style="top:190px;width:350px;">Our workplaces are safe :</h2>
  <div class="copy" style="top:238px;">
    <p>There is nothing more important to us than our people going home healthy and safe every day. We won’t accept anything less. We believe safety is a management choice. By providing safe work systems, and education we achieve our daily goal of Zero Harm. At Fernvale Land Care we,</p>
    <ul class="bullets" style="margin-top:10px;">
      <li>Take the time to make our work areas safe, whatever it takes.</li>
      <li>Don’t accept shortcuts.</li>
      <li>Look out for each other.</li>
      <li>Investigate our incidents and learn from them, we won’t accept repeats.</li>
      <li>Are constantly looking for ways to improve the safety of our workplaces.</li>
      <li>Think safe, work safer, go home safe!</li>
    </ul>
  </div>

  <h2 class="section-tab" style="top:438px;width:350px;">We give back :</h2>
  <div class="copy" style="top:490px;font-size:12.5px;">
    <p>We appreciate our success and we give back by supporting our community, and those less fortunate.</p>
  </div>

  <div class="footer-contact" style="left:40px;top:640px;">
    <svg width="14" height="14" viewBox="0 0 24 24" fill="#fff"><path d="M6.6 10.8a15.1 15.1 0 0 0 6.6 6.6l2.2-2.2c.3-.3.7-.4 1-.2 1.1.4 2.3.6 3.6.6.6 0 1 .4 1 1V20c0 .6-.4 1-1 1A17 17 0 0 1 3 4c0-.6.4-1 1-1h3.5c.6 0 1 .4 1 1 0 1.3.2 2.5.6 3.6.1.3 0 .7-.2 1z"/></svg>
    <span>07 4600 1234</span>
  </div>
  <div class="footer-contact" style="left:40px;top:668px;">
    <svg width="14" height="16" viewBox="0 0 24 24" fill="#fff"><path d="M12 2a7 7 0 0 0-7 7c0 5.3 7 13 7 13s7-7.7 7-13a7 7 0 0 0-7-7zm0 9.5A2.5 2.5 0 1 1 12 6.5a2.5 2.5 0 0 1 0 5z"/></svg>
    <span>Fernvale Land Care Pty Ltd.<br>P.O Box 1150 Brookfield, QLD</span>
  </div>
  <div class="footer-contact" style="left:300px;top:600px;">
    <svg width="16" height="12" viewBox="0 0 24 18" fill="none" stroke="#fff" stroke-width="2"><rect x="1" y="1" width="22" height="16"/><path d="M1 1l11 9 11-9"/></svg>
    <span>info@fernvaleland.com.au</span>
  </div>
  <div class="footer-contact" style="left:300px;top:630px;">
    <svg width="18" height="16" viewBox="0 0 24 22" fill="#fff"><path d="M12 1L1 11h3v10h6v-6h4v6h6V11h3z"/></svg>
    <span>Unit 2, 8-12 Wattle Lane<br>Hillcrest QLD 4300</span>
  </div>
</section>

</body>
</html>
```